Packaging Design for Face Mask Box

We are looking for an attractive but subtle packaging design for Face Masks (for non medical use). 50pcs per box.

The brand name should be "Kelvano". We have not yet got a logo or a text selected (font) for the brand name so we are open to your ideas on how "Kelvano" could look. It could have some elements of fresh air or breathing etc so symbolize clean and healthier air or something along those lines.

The box dimensions should be 180mm (L) x 100mm (W) x 90mm (H).

The box should have a perforation on top - exactly similar to Tissue Box packs. So, in order to access the face masks, the user should tear off the perforation and extract one mask at a time.

As this is not a medical grade face mask, the product should indicate "For Non- Medical Use". Also the heading of the masks should be DISPOSABLE PROTECTIVE FACE MASKS with sub heading 3 PLY FACE MASKS WITH EAR LOOP.

We will also prefer to have the Instructions to use and Precautions which are commonly available on face mask packages. This could be printed either on the sides or on the bottom of the package. There should also be a blank space on one of the sides to print Batch No. Mfg Date and Exp Date.

The box design could have some design resemblance to our company logo which is hereby attached in high resolution. However this is not compulsory.

The following phrases could be mentioned on the box to highlight some of the product features:

Dual Charge Electrostatic fibres for extra filtration
Improved Nose Bridge Strips for better protection
Tri-layer barrier with 3 x 25 g/m2 material
In-house production of filter material for Quality Consistency

I have added 3 samples face mask box designs from other manufacturers for your reference to get an idea of the box shape etc.

If you have any more questions, please feel free to ask.

Good luck!

```html
<!DOCTYPE html>
<html lang="en">
<head>
<meta charset="utf-8">
<title>Kelvano Face Mask Box – Dieline</title>
<link rel="stylesheet" href="https://fonts.googleapis.com/css2?family=Montserrat:wght@500;700&display=swap">
<style>
  :root {
    --paper: #ffffff;
    --cut-line: #8a8a8a;
    --night-deep: #05101c;
    --night-mid: #0d2a40;
    --mask-white: #dfe7ee;
    --brand-blue: #2b5f9e;
    --accent-orange: #f6b059;
    --text-light: #ffffff;
    --text-dark: #13273a;
    --perforation: #9fc3d6;
  }
  html, body {
    margin: 0;
    padding: 0;
    width: 1200px;
    height: 521px;
    overflow: hidden;
    background: var(--paper);
  }
  .dieline { display: block; width: 1200px; height: 521px; }
  .cut { fill: var(--paper); stroke: var(--cut-line); stroke-width: 1; }
  .rule { stroke: #222; stroke-width: 1.2; }
  .perforation { fill: none; stroke: var(--perforation); stroke-width: 1.2; stroke-dasharray: 5 4; }
  .brand-name { font-family: "Montserrat", sans-serif; font-weight: 700; font-size: 13px; fill: var(--brand-blue); }
  .brand-name-light { font-family: "Montserrat", sans-serif; font-weight: 700; font-size: 13px; fill: var(--text-light); }
  .headline { font-family: "Montserrat", sans-serif; font-weight: 700; font-size: 10.5px; fill: var(--text-light); }
  .tag-label { font-family: "Montserrat", sans-serif; font-weight: 700; font-size: 7.4px; fill: var(--text-light); }
  .tear-label { font-family: "Montserrat", sans-serif; font-weight: 500; font-size: 8px; fill: var(--perforation); letter-spacing: 1px; }
  .panel-title { font-family: "Montserrat", sans-serif; font-weight: 700; font-size: 9px; fill: var(--brand-blue); }
  .panel-copy { font-family: "Montserrat", sans-serif; font-weight: 500; font-size: 7px; fill: var(--text-dark); }
  .strip-copy { font-family: "Montserrat", sans-serif; font-weight: 700; font-size: 8.5px; fill: var(--text-dark); letter-spacing: 0.5px; }
  .batch-box { fill: none; stroke: var(--text-dark); stroke-width: 0.8; }
</style>
</head>
<body>
<svg class="dieline" viewBox="0 0 1357 589" preserveAspectRatio="none" xmlns="http://www.w3.org/2000/svg">
  <defs>
    <radialGradient id="night-glow" cx="55%" cy="45%" r="75%">
      <stop offset="0" stop-color="var(--night-mid)"/>
      <stop offset="1" stop-color="var(--night-deep)"/>
    </radialGradient>
    <radialGradient id="mask-glow" cx="50%" cy="50%" r="50%">
      <stop offset="0" stop-color="var(--mask-white)" stop-opacity="0.9"/>
      <stop offset="0.7" stop-color="var(--mask-white)" stop-opacity="0.35"/>
      <stop offset="1" stop-color="var(--mask-white)" stop-opacity="0"/>
    </radialGradient>
    <clipPath id="front-clip"><rect x="90" y="245" width="415" height="176"/></clipPath>
  </defs>

  <!-- glue flap -->
  <path class="cut" d="M90 245 L72 252 L70 440 L90 453 Z"/>

  <!-- lid panel with tear-off opening -->
  <path class="cut" d="M90 245 V38 Q90 18 110 18 H485 Q505 18 505 38 V245 Z"/>
  <path d="M90 245 V38 Q90 18 110 18 H485 Q505 18 505 38 V245 Z" fill="url(#night-glow)"
        role="img" aria-label="Dark blue backdrop with softly glowing teal virus particles"/>
  <rect class="perforation" x="177" y="95" width="240" height="70" rx="35"/>
  <text class="tear-label" x="297" y="134" text-anchor="middle">TEAR HERE</text>
  <text class="brand-name-light" x="297" y="210" text-anchor="middle">Kelvano</text>

  <!-- front panel -->
  <rect class="cut" x="90" y="245" width="415" height="208"/>
  <g role="img" aria-label="Disposable three-ply face mask floating among teal virus particles on a dark blue backdrop">
    <rect x="90" y="245" width="415" height="176" fill="url(#night-glow)"/>
    <ellipse cx="380" cy="333" rx="110" ry="80" fill="url(#mask-glow)"/>
  </g>
  <g clip-path="url(#front-clip)">
    <circle cx="150" cy="275" r="63" fill="var(--paper)"/>
  </g>
  <rect x="115" y="288" width="9" height="9" fill="var(--brand-blue)"/>
  <text class="brand-name" x="128" y="297">Kelvano</text>
  <text class="headline" x="110" y="358">DISPOSABLE PROTECTIVE</text>
  <text class="headline" x="110" y="370">FACE MASKS</text>
  <rect x="110" y="377" width="133" height="15" fill="var(--accent-orange)"/>
  <text class="tag-label" x="176.5" y="387.5" text-anchor="middle">3 PLY FACE MASKS WITH EAR LOOP</text>
  <text class="strip-copy" x="297.5" y="441" text-anchor="middle">FOR NON-MEDICAL USE · 50 PCS</text>

  <!-- side panel one: instructions -->
  <path class="cut" d="M505 245 L512 238 L516 207 H684 L688 238 L694 245 Z"/>
  <rect class="cut" x="505" y="245" width="189" height="208"/>
  <path class="cut" d="M505 453 L520 470 L528 547 H663 L694 453 Z"/>
  <g class="instructions">
    <text class="panel-title" x="518" y="272">INSTRUCTIONS FOR USE</text>
    <text class="panel-copy" x="518" y="292">1. Wash hands before handling the mask.</text>
    <text class="panel-copy" x="518" y="307">2. Coloured side faces outward.</text>
    <text class="panel-copy" x="518" y="322">3. Place ear loops around each ear.</text>
    <text class="panel-copy" x="518" y="337">4. Press the nose strip to fit snugly.</text>
    <text class="panel-copy" x="518" y="352">5. Cover nose, mouth and chin fully.</text>
    <text class="panel-copy" x="518" y="367">6. Remove by ear loops and discard.</text>
  </g>

  <!-- back panel -->
  <rect class="cut" x="694" y="245" width="416" height="208"/>
  <g role="img" aria-label="Disposable three-ply face mask floating among teal virus particles on a dark blue backdrop">
    <rect x="694" y="245" width="416" height="176" fill="url(#night-glow)"/>
    <ellipse cx="985" cy="333" rx="110" ry="80" fill="url(#mask-glow)"/>
  </g>
  <text class="strip-copy" x="902" y="441" text-anchor="middle">FOR NON-MEDICAL USE · 50 PCS</text>

  <!-- side panel two: precautions and batch details -->
  <path class="cut" d="M1110 245 L1116 238 L1121 207 H1289 L1293 238 L1299 245 Z"/>
  <rect class="cut" x="1110" y="245" width="189" height="208"/>
  <path class="cut" d="M1110 453 L1125 470 L1133 547 H1268 L1299 453 Z"/>
  <g class="precautions">
    <text class="panel-title" x="1123" y="272">PRECAUTIONS</text>
    <text class="panel-copy" x="1123" y="290">• Single use only. Do not wash or reuse.</text>
    <text class="panel-copy" x="1123" y="304">• Replace if damp, soiled or damaged.</text>
    <text class="panel-copy" x="1123" y="318">• Not for medical or surgical use.</text>
    <text class="panel-copy" x="1123" y="332">• Store in a cool, dry place.</text>
    <text class="panel-copy" x="1123" y="346">• Keep away from fire and heat.</text>
    <rect class="batch-box" x="1123" y="362" width="163" height="56"/>
    <text class="panel-copy" x="1130" y="377">Batch No:</text>
    <text class="panel-copy" x="1130" y="394">Mfg Date:</text>
    <text class="panel-copy" x="1130" y="411">Exp Date:</text>
  </g>

  <!-- bottom flaps -->
  <path class="cut" d="M90 453 H505 V566 H428 L405 540 H310 L287 566 H90 Z"/>
  <path class="cut" d="M694 453 H1110 V566 H1032 L1009 540 H914 L891 566 H694 Z"/>
  <g class="features">
    <text class="panel-title" x="108" y="475">PRODUCT FEATURES</text>
    <text class="panel-copy" x="108" y="491">• Dual Charge Electrostatic fibres for extra filtration</text>
    <text class="panel-copy" x="108" y="504">• Improved Nose Bridge Strips for better protection</text>
    <text class="panel-copy" x="108" y="517">• Tri-layer barrier with 3 x 25 g/m² material</text>
    <text class="panel-copy" x="108" y="530">• In-house production of filter material for Quality Consistency</text>
  </g>
  <text class="panel-title" x="902" y="490" text-anchor="middle">Kelvano</text>
  <text class="panel-copy" x="902" y="506" text-anchor="middle">Disposable Protective Face Masks · 50 pcs per box</text>

  <line class="rule" x1="0" y1="588" x2="1357" y2="588"/>
</svg>
</body>
</html>
```